Business Card for a mobile physiotherapy company

I need a layout for a business card for a mobile physiotherapy company.
Slogan is "Mobile Physiotherapy - Your Road To Recovery"
Phone number is 867-402-5913
Email VantrePhysio@mailbright.ca (subject to change with website)
Website www.VantrePhysio.ca
My name and credentials: Kent Vantre Kent Vantre, BSc(kin), MPT, CAFCI, IMS
Information maybe included: Direct Billing, Services including Physiotherapy, IMS, acupuncture
Maybe include facebook and instagram logos
One side with the logo clean and sharp
Other side with details, try not to look too busy, keep everything concise

```html
<!DOCTYPE html>
<html lang="en">
<head>
<meta charset="utf-8">
<title>Vantre Physio Business Card</title>
<link href="https://fonts.googleapis.com/css2?family=Libre+Baskerville:wght@700&family=Roboto:wght@400;500&display=swap" rel="stylesheet">
<style>
  :root {
    --navy: #25497f;
    --green: #135a48;
    --paper: #f7f7f5;
    --ink: #2b2b2b;
    --backdrop: #2a2a2c;
  }
  * { box-sizing: border-box; margin: 0; padding: 0; }
  html, body { width: 1200px; height: 800px; overflow: hidden; }
  body {
    background: var(--backdrop);
    font-family: "Roboto", Arial, sans-serif;
    position: relative;
  }
  .card {
    position: absolute;
    left: 320px;
    width: 560px;
    height: 320px;
    background: var(--paper);
    overflow: hidden;
    box-shadow: 0 14px 30px rgba(0,0,0,0.45);
  }
  .card-front { top: 50px; }
  .card-back { top: 430px; }

  /* wordmark */
  .wordmark {
    position: absolute;
    display: flex;
    align-items: center;
    gap: 10px;
    font-family: "Libre Baskerville", Georgia, serif;
    font-weight: 700;
    color: var(--green);
  }
  .wordmark-dot {
    border-radius: 50%;
    background: var(--navy);
    flex: none;
  }
  .card-front .wordmark {
    left: 0; right: 0; top: 92px;
    justify-content: center;
    font-size: 32px;
    letter-spacing: 3px;
  }
  .card-front .wordmark-dot { width: 34px; height: 34px; }
  .card-back .wordmark {
    left: 44px; top: 34px;
    font-size: 17px;
    letter-spacing: 2px;
  }
  .card-back .wordmark-dot { width: 20px; height: 20px; }

  /* bands */
  .band-navy { position: absolute; background: var(--navy); }
  .band-green { position: absolute; background: var(--green); }
  .strip-green { position: absolute; left: 0; right: 0; bottom: 0; height: 14px; background: var(--green); }

  .card-front .band-navy { left: 0; right: 0; top: 232px; bottom: 0; }
  .slogan-tab {
    position: absolute;
    left: 108px; width: 344px;
    top: 214px; height: 58px;
    background: var(--green);
    border-radius: 20px 20px 0 0;
    color: #ffffff;
    font-size: 14.5px;
    display: flex; align-items: center; justify-content: center;
  }

  /* back details */
  .holder-name {
    position: absolute;
    left: 44px; top: 96px;
    font-family: "Libre Baskerville", Georgia, serif;
    font-weight: 700;
    font-size: 19px;
    color: var(--navy);
  }
  .credentials {
    position: absolute;
    left: 44px; top: 124px;
    font-size: 13px;
    color: var(--ink);
  }
  .rule { position: absolute; height: 1.5px; background: var(--navy); }
  .rule-top { left: 290px; right: 40px; top: 98px; }
  .rule-under { left: 44px; width: 230px; top: 148px; }

  .contact-list {
    position: absolute;
    left: 44px; top: 160px;
    list-style: none;
  }
  .contact-list li {
    display: flex; align-items: center; gap: 12px;
    font-size: 13.5px;
    color: var(--ink);
    height: 22px;
  }
  .contact-list svg { width: 13px; height: 13px; fill: var(--green); flex: none; }

  .card-back .band-navy { left: 0; width: 410px; top: 252px; bottom: 0; }
  .social-tab {
    position: absolute;
    left: 400px; right: 0;
    top: 222px; bottom: 0;
    background: var(--green);
    border-radius: 28px 0 0 0;
  }
  .social-links {
    position: absolute;
    right: 34px; top: 188px;
    display: flex; gap: 10px;
  }
  .social-dot {
    width: 22px; height: 22px;
    border-radius: 50%;
    border: 2px solid var(--green);
    background: #ffffff;
  }
</style>
</head>
<body>

<section class="card card-front" aria-label="Card front">
  <div class="wordmark"><span class="wordmark-dot"></span>VANTRE PHYSIO</div>
  <div class="band-navy"></div>
  <div class="slogan-tab">Mobile Physiotherapy - Your Road To Recovery</div>
  <div class="strip-green"></div>
</section>

<section class="card card-back" aria-label="Card back">
  <div class="wordmark"><span class="wordmark-dot"></span>VANTRE PHYSIO</div>
  <div class="rule rule-top"></div>
  <h1 class="holder-name">Kent Vantre Kent Vantre</h1>
  <p class="credentials">BSc(kin), MPT, CAFCI, IMS</p>
  <div class="rule rule-under"></div>
  <ul class="contact-list">
    <li>
      <svg viewBox="0 0 24 24" aria-hidden="true"><path d="M6.6 10.8a15.1 15.1 0 0 0 6.6 6.6l2.2-2.2c.3-.3.7-.4 1-.2 1.1.4 2.3.6 3.6.6.6 0 1 .4 1 1V20c0 .6-.4 1-1 1A17 17 0 0 1 3 4c0-.6.4-1 1-1h3.5c.6 0 1 .4 1 1 0 1.3.2 2.5.6 3.6.1.3 0 .7-.2 1z"/></svg>
      867-402-5913
    </li>
    <li>
      <svg viewBox="0 0 24 24" aria-hidden="true"><path d="M2 5h20v14H2z M2 5l10 8 10-8" fill="none" stroke="#135a48" stroke-width="0"/><path d="M2 5h20L12 12.5z"/><path d="M2 7.2l10 7.8 10-7.8V19H2z"/></svg>
      VantrePhysio@mailbright.ca
    </li>
    <li>
      <svg viewBox="0 0 24 24" aria-hidden="true"><circle cx="12" cy="12" r="10" fill="none" stroke="#135a48" stroke-width="2"/><ellipse cx="12" cy="12" rx="4" ry="10" fill="none" stroke="#135a48" stroke-width="2"/><path d="M2 12h20" stroke="#135a48" stroke-width="2"/></svg>
      www.VantrePhysio.ca
    </li>
  </ul>
  <div class="social-links" aria-label="Social media">
    <span class="social-dot"></span>
    <span class="social-dot"></span>
  </div>
  <div class="band-navy"></div>
  <div class="social-tab"></div>
  <div class="strip-green"></div>
</section>

</body>
</html>
```